Letterhead Design for Corvane Communications

We are a Telecommunications Company, We wanting to get our Letterhead sorted as the one we have now looks Dull, It be used across our different databases we use but also mainly in Word , I have attached our Logo for you also, our website is corvane-example.com.au

We would only like to show our postal Address which is PO Box 8142 Tilford Cove NSW 2497

and we need to show our ABN Number Which we would be ABN: 61 804 327 918

Target Market(s)

Looks Stunning for our Proposals and General Usage

Industry/Entity Type

Telecommunications

Requirements
Must have
• Our Postal Address Only and Our ABN Number
Should not have
• Not listing our Actual Address

```html
<!DOCTYPE html>
<html lang="en">
<head>
<meta charset="utf-8">
<title>Corvane Communications Letterhead</title>
<link rel="stylesheet" href="https://fonts.googleapis.com/css2?family=Open+Sans:wght@400;700&display=swap">
<style>
  :root {
    --backdrop: #e4e4e2;
    --paper: #f8f8f6;
    --orange: #e2622c;
    --green: #3cc43f;
    --text: #4a4a48;
    --ink: #ffffff;
  }
  * { margin: 0; padding: 0; box-sizing: border-box; }
  html, body {
    width: 1008px;
    height: 1200px;
    overflow: hidden;
    background: var(--backdrop);
    font-family: "Open Sans", sans-serif;
  }
  .letterhead {
    position: absolute;
    left: 58px;
    top: 30px;
    width: 891px;
    height: 1140px;
    background: var(--paper);
    overflow: hidden;
    box-shadow: 0 10px 30px rgba(0, 0, 0, 0.18);
  }
  .corner-decor {
    position: absolute;
    display: block;
  }
  .corner-decor--top {
    left: 0;
    top: 0;
    width: 340px;
    height: 210px;
  }
  .corner-decor--bottom {
    right: 0;
    bottom: 0;
    width: 498px;
    height: 207px;
  }
  .brand {
    position: absolute;
    left: 474px;
    top: 106px;
    display: flex;
    align-items: center;
    gap: 12px;
  }
  .brand__dot {
    width: 92px;
    height: 92px;
    border-radius: 50%;
    background: var(--orange);
    flex: none;
  }
  .brand__name {
    font-weight: 700;
    font-size: 22px;
    line-height: 1.15;
    color: var(--orange);
    letter-spacing: 0.04em;
    text-transform: uppercase;
    width: 230px;
  }
  .contact {
    position: absolute;
    left: 28px;
    bottom: 72px;
    font-size: 12px;
    line-height: 1.5;
    color: var(--text);
  }
  .contact__label {
    font-weight: 700;
    color: var(--orange);
  }
  .web-tab {
    position: absolute;
    left: 0;
    bottom: 0;
    width: 330px;
    height: 58px;
    background: var(--orange);
    border-top-right-radius: 30px;
    display: flex;
    align-items: center;
    gap: 8px;
    padding-left: 28px;
    color: var(--ink);
  }
  .web-tab__icon { width: 18px; height: 18px; flex: none; }
  .web-tab__url {
    font-weight: 700;
    font-size: 15px;
    white-space: nowrap;
  }
</style>
</head>
<body>
  <main class="letterhead">
    <svg class="corner-decor corner-decor--top" role="img" aria-label="Decorative orange and green corner graphic" viewBox="0 0 340 210" preserveAspectRatio="none">
      <defs>
        <linearGradient id="decorTop" x1="0" y1="0" x2="1" y2="1">
          <stop offset="0" stop-color="#e8844f" stop-opacity="0.55"/>
          <stop offset="1" stop-color="#3cc43f" stop-opacity="0"/>
        </linearGradient>
      </defs>
      <rect width="340" height="210" fill="url(#decorTop)"/>
    </svg>

    <div class="brand">
      <span class="brand__dot"></span>
      <span class="brand__name">Corvane Communications</span>
    </div>

    <svg class="corner-decor corner-decor--bottom" role="img" aria-label="Decorative green and orange corner graphic" viewBox="0 0 498 207" preserveAspectRatio="none">
      <defs>
        <linearGradient id="decorBottom" x1="0" y1="1" x2="1" y2="0">
          <stop offset="0" stop-color="#3cc43f" stop-opacity="0"/>
          <stop offset="0.5" stop-color="#3cc43f" stop-opacity="0.45"/>
          <stop offset="1" stop-color="#e8844f" stop-opacity="0.6"/>
        </linearGradient>
      </defs>
      <rect width="498" height="207" fill="url(#decorBottom)"/>
    </svg>

    <address class="contact">
      <span class="contact__line">PO Box 8142 Tilford Cove NSW 2497</span><br>
      <span class="contact__line"><span class="contact__label">ABN:</span> 61 804 327 918</span>
    </address>

    <footer class="web-tab">
      <svg class="web-tab__icon" viewBox="0 0 20 20" fill="none" stroke="#ffffff" stroke-width="1.4" aria-hidden="true">
        <circle cx="10" cy="10" r="8.5"/>
        <ellipse cx="10" cy="10" rx="3.8" ry="8.5"/>
        <line x1="1.5" y1="10" x2="18.5" y2="10"/>
        <line x1="3" y1="5.5" x2="17" y2="5.5"/>
        <line x1="3" y1="14.5" x2="17" y2="14.5"/>
      </svg>
      <span class="web-tab__url">www.corvane-example.com.au</span>
    </footer>
  </main>
</body>
</html>
```